Business Card Design Project

looking for business cards with new logo

I am looking to keep with the colors of the logo i posted.  Here are some other details to consider.  I would like my website prominently displayed on the business card with the logo.  my website is www.PRopelVK.com...it should be spelled this way.

My contact information is:

Daniel J Whitcombe III
Broker/Owner
4587 Larkspur Ave., Suite 308
Brookvale, Texas 78451
Office: 830-419-5576
Email:  Daniel@PRopelVK.com

Thank you
Daniel Whitcombe

```html
<!DOCTYPE html>
<html lang="en">
<head>
<meta charset="utf-8">
<title>Propel Realty – Business Cards</title>
<link href="https://fonts.googleapis.com/css2?family=Fira+Sans:wght@400;500;600&display=swap" rel="stylesheet">
<style>
  :root {
    --stage: #2b2b2d;
    --navy: #164372;
    --sky: #3ea6e0;
    --paper: #f4f4f5;
    --white: #ffffff;
    --ink: #1f3550;
  }
  * { box-sizing: border-box; margin: 0; padding: 0; }
  html, body { width: 1200px; height: 900px; overflow: hidden; }
  body {
    background: var(--stage);
    font-family: "Fira Sans", Arial, sans-serif;
    position: relative;
  }
  .card {
    position: absolute;
    width: 500px;
    height: 286px;
    top: 307px;
    overflow: hidden;
    box-shadow: 0 10px 30px rgba(0,0,0,.55);
  }
  /* Front */
  .card--front {
    left: 60px;
    background: var(--navy);
    display: flex;
    flex-direction: column;
    align-items: center;
    justify-content: center;
    gap: 26px;
  }
  .brand {
    display: flex;
    align-items: center;
    gap: 10px;
    font-weight: 500;
    font-size: 40px;
    letter-spacing: .5px;
    line-height: 1;
    white-space: nowrap;
  }
  .brand__mark { width: 16px; height: 16px; flex: none; }
  .card--front .brand { color: var(--white); }
  .card--front .brand__mark { background: var(--sky); }
  .website {
    color: var(--white);
    font-size: 17px;
    font-weight: 500;
    letter-spacing: .3px;
  }
  .website__name { color: var(--sky); }

  /* Back */
  .card--back { left: 640px; background: var(--navy); }
  .back__top {
    position: absolute;
    inset: 0 0 auto 0;
    height: 118px;
    background: var(--paper);
    display: flex;
    align-items: center;
    padding-left: 70px;
  }
  .card--back .brand { color: var(--ink); font-size: 34px; }
  .card--back .brand__mark { background: var(--sky); width: 14px; height: 14px; }
  .back__rule {
    position: absolute;
    left: 0; right: 0; top: 118px;
    height: 5px;
    background: var(--sky);
  }
  .back__notch { position: absolute; left: 58px; top: 121px; }
  .contact { position: absolute; color: var(--white); }
  .contact__person { left: 48px; top: 146px; }
  .contact__name { color: var(--sky); font-size: 16px; font-weight: 500; }
  .contact__title { font-size: 11px; margin-top: 3px; }
  .contact__address { font-size: 11.5px; line-height: 1.35; margin-top: 12px; }
  .contact__lines { right: 30px; bottom: 28px; font-size: 13px; line-height: 1.45; }
  .contact__label { color: var(--sky); display: inline-block; width: 44px; }
</style>
</head>
<body>
  <section class="card card--front" aria-label="Card front">
    <div class="brand"><span class="brand__mark"></span>Propel Realty</div>
    <p class="website">www.<span class="website__name">PRopelVK</span>.com</p>
  </section>

  <section class="card card--back" aria-label="Card back">
    <div class="back__top">
      <div class="brand"><span class="brand__mark"></span>Propel Realty</div>
    </div>
    <div class="back__rule"></div>
    <svg class="back__notch" width="24" height="12" viewBox="0 0 24 12" aria-hidden="true">
      <polygon points="0,0 24,0 12,12" fill="var(--sky)"/>
      <polygon points="5,0 19,0 12,7" fill="var(--paper)"/>
    </svg>

    <div class="contact contact__person">
      <p class="contact__name">Daniel J Whitcombe III</p>
      <p class="contact__title">Broker/Owner</p>
      <p class="contact__address">4587 Larkspur Ave., Suite 308<br>Brookvale, Texas 78451</p>
    </div>

    <div class="contact contact__lines">
      <p><span class="contact__label">Office:</span> 830-419-5576</p>
      <p><span class="contact__label">Email:</span> Daniel@PRopelVK.com</p>
    </div>
  </section>
</body>
</html>
```